Business card design for Bront Engineering Qavo

We need a new business card design along with all the necessary to place an order. The company is Bront Engineering Qavo and we recently updated our logo.

```html
<!DOCTYPE html>
<html lang="en">
<head>
<meta charset="utf-8">
<title>Bront Engineering Qavo – Business Card</title>
<link href="https://fonts.googleapis.com/css2?family=Mulish:wght@400;600;800&display=swap" rel="stylesheet">
<style>
  :root {
    --backdrop: #2a2a2c;
    --yellow: #e1bb22;
    --ink: #1c1c1c;
    --grey: #9a9a9a;
    --band: #9c9c9c;
    --text: #3a3a3a;
    --white: #ffffff;
  }
  * { margin: 0; padding: 0; box-sizing: border-box; }
  html, body { width: 1200px; height: 982px; overflow: hidden; }
  body {
    background: var(--backdrop);
    font-family: "Mulish", sans-serif;
    display: flex;
    flex-direction: column;
    align-items: center;
    justify-content: center;
    gap: 36px;
  }
  .card {
    width: 735px;
    height: 420px;
    border-radius: 28px;
    position: relative;
    overflow: hidden;
  }
  .card-front {
    background: var(--yellow);
    display: flex;
    align-items: center;
    justify-content: center;
  }
  .wordmark {
    display: flex;
    align-items: center;
    gap: 16px;
    font-weight: 800;
    letter-spacing: 0.04em;
    text-transform: uppercase;
  }
  .wordmark-mark { width: 34px; height: 34px; flex: none; }
  .card-front .wordmark { color: var(--ink); font-size: 40px; }
  .card-front .wordmark-mark { background: var(--ink); }

  .card-back { background: var(--white); }
  .name-band {
    position: absolute;
    left: 0; top: 58px;
    width: 500px; height: 112px;
  }
  .name-band svg { position: absolute; inset: 0; }
  .name-block { position: absolute; left: 56px; top: 76px; color: var(--white); }
  .person-name { font-size: 38px; font-weight: 800; letter-spacing: 0.01em; line-height: 1.05; text-transform: uppercase; }
  .person-role { font-size: 20px; font-weight: 400; margin-top: 4px; }

  .card-back .wordmark {
    position: absolute;
    right: 48px; top: 200px;
    color: var(--grey);
    font-size: 27px;
    gap: 12px;
  }
  .card-back .wordmark-mark { width: 24px; height: 24px; background: var(--yellow); }

  .contact-list {
    position: absolute;
    left: 52px; top: 270px;
    list-style: none;
    font-size: 20px;
    color: var(--text);
    line-height: 1.6;
  }
  .contact-list li { display: flex; align-items: center; gap: 14px; }
  .contact-list svg { width: 18px; height: 18px; fill: var(--yellow); flex: none; }

  .address {
    position: absolute;
    right: 48px; bottom: 40px;
    text-align: right;
    font-size: 20px;
    line-height: 1.5;
    color: var(--text);
    font-style: normal;
  }
</style>
</head>
<body>

  <section class="card card-front">
    <div class="wordmark">
      <span class="wordmark-mark"></span>
      <span class="wordmark-name">Bront Engineering Qavo</span>
    </div>
  </section>

  <section class="card card-back">
    <div class="name-band">
      <svg viewBox="0 0 500 112" preserveAspectRatio="none" aria-hidden="true">
        <polygon points="0,0 440,0 500,112 0,112" fill="var(--band)"/>
      </svg>
    </div>
    <div class="name-block">
      <div class="person-name">Daniel Harper</div>
      <div class="person-role">Founder &amp; CEO</div>
    </div>

    <div class="wordmark">
      <span class="wordmark-mark"></span>
      <span class="wordmark-name">Bront Engineering Qavo</span>
    </div>

    <ul class="contact-list">
      <li>
        <svg viewBox="0 0 24 24" aria-hidden="true"><path d="M6.6 10.8a15.1 15.1 0 0 0 6.6 6.6l2.2-2.2c.3-.3.7-.4 1-.2 1.1.4 2.3.6 3.6.6.6 0 1 .4 1 1V20c0 .6-.4 1-1 1A17 17 0 0 1 3 4c0-.6.4-1 1-1h3.5c.6 0 1 .4 1 1 0 1.3.2 2.5.6 3.6.1.3 0 .7-.2 1z"/></svg>
        (555) 210-4830
      </li>
      <li>
        <svg viewBox="0 0 24 24" aria-hidden="true"><path d="M7 1h10a2 2 0 0 1 2 2v18a2 2 0 0 1-2 2H7a2 2 0 0 1-2-2V3a2 2 0 0 1 2-2zm0 3v14h10V4zm5 15.5a1 1 0 1 0 0 2 1 1 0 0 0 0-2z"/></svg>
        (555) 210-4831
      </li>
      <li>
        <svg viewBox="0 0 24 24" aria-hidden="true"><path d="M6 2h12v5H6zM4 8h16a2 2 0 0 1 2 2v7h-4v5H6v-5H2v-7a2 2 0 0 1 2-2zm4 8v4h8v-4z"/></svg>
        (555) 210-4832
      </li>
      <li>
        <svg viewBox="0 0 24 24" aria-hidden="true"><path d="M2 5h20v14H2zm2 2v.5l8 5 8-5V7z"/></svg>
        hello@brontqavo.com
      </li>
    </ul>

    <address class="address">
      Bront Engineering Qavo<br>
      423 Street Address Here, City<br>
      State, Country, ZIP Code<br>
      www.brontqavo.com
    </address>
  </section>

</body>
</html>
```